Marou Cay Lodge Christmas wishes 2013

We require postcards designed to mail our to our clients for Christmas. We are a SURF travel company, with a high end market and like to mail our Christmas postcards to all our guests that have stayed with us through the year. Front cover will have images and text (ie Seasons Greeting) and our logo. The back will have space for TO: name & address and postage stamp. Will also have some basic text (ie The Management & Staff at Marou Cay Lodge wish you and your family all the best for the Festive Season and New Year. We look forward to seeing you back at Marou Cay Lodge again soon etc etc). Here is link to main image https://www.filevault-example.com/sh/qwmzrtpx318kle/Zr8pWnQvcB

Target Market(s)

Our clients are mostly mature men (40-70) surfers who purchase luxury surf trips

Industry/Entity Type

Travel

Requirements
Must have
• Ocean Image (front)
Logo x 2 in same colour - Halcyra & Marou Cay Lodge (front)
Text (front)
Back to be white
Space for name & address (back)
Space for postage stamp (back)
Message (back)
Website www.halcyralodges-example.com (back)

```html
<!DOCTYPE html>
<html lang="en">
<head>
<meta charset="utf-8">
<title>Marou Cay Lodge – Season's Greetings Postcard</title>
<link rel="stylesheet" href="https://fonts.googleapis.com/css2?family=Nunito:wght@400;700;800&family=Nunito+Sans:wght@300;400&display=swap">
<style>
  :root {
    --backdrop: #e27529;
    --card-white: #ffffff;
    --ink: #2b2b2b;
    --stamp-grey: #acacac;
    --photo-sky: #b8822c;
    --photo-glow: #f6d27a;
    --photo-dark: #0b0906;
    --on-photo: #ffffff;
    --on-photo-soft: #d9d4cc;
  }
  * { margin: 0; padding: 0; box-sizing: border-box; }
  html, body {
    width: 1200px; height: 1000px; overflow: hidden;
    background: var(--backdrop);
  }
  .canvas { position: relative; width: 1200px; height: 1000px; }

  /* Front of postcard */
  .postcard-front {
    position: absolute; left: 321px; top: 57px; width: 566px; height: 376px;
    overflow: hidden;
  }
  .front-photo {
    position: absolute; inset: 0;
    background:
      radial-gradient(circle at 74% 52%, var(--photo-glow) 0, #e2a84a 12%, rgba(184,130,44,0) 38%),
      linear-gradient(180deg, #4a3518 0%, var(--photo-sky) 45%, #6a4a1c 68%, var(--photo-dark) 86%);
  }
  .front-greeting {
    position: absolute; left: 70px; top: 167px;
    font: 800 22px/1 "Nunito", sans-serif; color: var(--on-photo);
    letter-spacing: -0.2px; white-space: nowrap;
  }
  .lodge-mark {
    position: absolute; left: 58px; top: 304px; width: 200px; text-align: center;
    color: var(--on-photo-soft); font-family: "Nunito Sans", sans-serif;
    white-space: nowrap;
  }
  .lodge-mark .mark-dot {
    display: block; width: 26px; height: 26px; margin: 0 auto 6px;
    border: 2px solid var(--on-photo-soft); border-radius: 50%;
  }
  .lodge-mark .mark-name { display: block; font-size: 11px; line-height: 13px; font-weight: 400; }
  .lodge-mark .mark-country { display: block; font-size: 8px; line-height: 10px; font-weight: 400; letter-spacing: 1px; margin-top: 1px; }
  .group-mark {
    position: absolute; left: 289px; top: 324px;
    display: flex; align-items: center; gap: 12px;
    color: var(--on-photo-soft); font: 400 11px/1 "Nunito Sans", sans-serif;
    letter-spacing: 1.6px; white-space: nowrap;
  }
  .group-mark .mark-dot {
    width: 18px; height: 18px; border: 2px solid var(--on-photo-soft); border-radius: 50%;
  }

  /* Back of postcard */
  .postcard-back {
    position: absolute; left: 325px; top: 509px; width: 562px; height: 375px;
    background: var(--card-white); color: var(--ink);
    font-family: "Nunito", sans-serif;
  }
  .back-message {
    position: absolute; left: 37px; top: 96px; width: 170px;
    font-size: 10.5px; font-weight: 700; line-height: 14.5px; text-align: justify;
  }
  .back-message p + p { margin-top: 13px; }
  .back-website {
    position: absolute; left: 51px; top: 261px;
    font-size: 10.5px; font-weight: 700; letter-spacing: -0.4px; white-space: nowrap;
  }
  .address-fields {
    position: absolute; left: 243px; top: 94px;
    font-size: 12px; font-weight: 700; list-style: none;
  }
  .address-fields li + li { margin-top: 16px; }
  .stamp-box {
    position: absolute; left: 452px; top: 38px; width: 69px; height: 69px;
    border: 3px solid var(--stamp-grey);
  }
</style>
</head>
<body>
<main class="canvas">
  <section class="postcard-front">
    <div class="front-photo" role="img" aria-label="Silhouette of a surfer holding a surfboard on his head, standing on rocks before the ocean at golden sunset"></div>
    <h1 class="front-greeting">Seasons Greetings!</h1>
    <div class="lodge-mark">
      <span class="mark-dot"></span>
      <span class="mark-name">maroucaylodge-example.com</span>
      <span class="mark-country">indonesia</span>
    </div>
    <div class="group-mark">
      <span class="mark-dot"></span>
      <span class="mark-name">HALCYRA LODGES &amp; RESORTS</span>
    </div>
  </section>

  <section class="postcard-back">
    <div class="back-message">
      <p>The Management &amp; Staff at Marou Cay Lodge wish you and your family all the best for the Festive Season and New Year.</p>
      <p>We look forward to seeing you back at Marou Cay Lodge again soon!</p>
    </div>
    <div class="back-website">WWW.HALCYRALODGES-EXAMPLE.COM</div>
    <ul class="address-fields">
      <li>name</li>
      <li>address</li>
    </ul>
    <div class="stamp-box"></div>
  </section>
</main>
</body>
</html>
```